Business Card Design

I am in the progress of starting up my business.

Business Name - Kestrel Surface Cleaning

Services that we offer
- Driveway Cleaning
- Foot Path Cleaning
- Pebble & Normal Cement
- Gutter Clean Out
- Removal of Moss & Mould
- Moss & Mould treatment is also available
- Entertainment & Courtyard Area's etc
- Gutter Guard Installation
- Full roof restoration, We Only Use Brightwell Products
- (brightwell application licence, Includes a full 10 year full warrenty )

New Business Card Information - I would like to get rid of "We cover all maitland & Newcastle regions" And Change it to Newcastle Region Hunter Valley Region Nelson Bay Region And the List on the back I would also like to change to OUR SERVICES Driveway & Foot Path Cleaning Treatment & Removal Of Moss & Mould Entertainment & Deck Area's Pebble Crete & cemented Area's Factory & Office Fronts House Exterior (Windows, Veranda's, Brick Work) Roof & Gutter Cleaning Roof Restoration - Brightwell, Solvane Roof Shield 417 (Brightwell Application Licence, Includes Full 10 Year Warranty)

Industry/Entity Type

Business

Contact Information for Business Card

Kestrel Surface Washing
Water Blasting And Roof Restorations
ABN # 48 217 903 561
Phone # 0412958364
Contact Liam For A Free Quote
Cover Maitland & Newcastle Region's

[Can you please send me an email when you would like me to send through picture as this page wont allow me to add pictures]

Thanks Liam

Requirements
Must have
• Main details on the front of the business card and a picture or two. on the back of the business I would like the list of services that my company provide on the back
Nice to have
• I was hoping that on the front of the business I could have all the company information and details and maybe a picture or two if able to. On the back of the card I would like the services I provide listed but also not over crowded at the same time..

```html
<!DOCTYPE html>
<html lang="en">
<head>
<meta charset="utf-8">
<title>Kestrel Surface Cleaning – Business Card</title>
<link href="https://fonts.googleapis.com/css2?family=Open+Sans:ital,wght@0,600;0,800;1,700&family=Signika:wght@500;600&display=swap" rel="stylesheet">
<style>
  :root{
    --page:#e6e8ec;
    --blue-deep:#1b2f86;
    --blue-mid:#2a55b8;
    --blue-light:#3f8fdc;
    --white:#ffffff;
    --yellow:#f2e600;
    --ink:#111111;
    --pebble-a:#8a8a86;
    --pebble-b:#4c4c4a;
    --brick-a:#c9745c;
    --brick-b:#a9533f;
    --roof-a:#c9ccca;
    --roof-b:#7f8a86;
    --tree:#3f6a3a;
  }
  *{box-sizing:border-box;margin:0;padding:0}
  html,body{width:1200px;height:1200px;overflow:hidden;background:var(--page)}
  .canvas{position:relative;width:1200px;height:1200px}
  .card{position:absolute;left:120px;width:960px;height:540px;overflow:hidden;border-radius:6px;box-shadow:0 8px 24px rgba(0,0,0,.18);background:var(--white)}
  .card--back{top:40px}
  .card--front{top:620px}
  .card svg.card-art{position:absolute;inset:0;width:100%;height:100%}
  .photo{position:absolute}

  /* back */
  .services{position:absolute;left:0;top:22px;width:100%;text-align:center;color:var(--white);font-family:"Open Sans",sans-serif;font-weight:600}
  .services__title{font-size:25px;margin-bottom:8px}
  .services__line{font-size:19px;line-height:29px}
  .services__licence{font-size:19px;line-height:29px;color:var(--yellow)}

  /* front */
  .brand{position:absolute;left:40px;top:34px;color:var(--white);font-family:"Open Sans",sans-serif;font-weight:800;font-size:54px;letter-spacing:.5px;line-height:1}
  .tagline{position:absolute;left:70px;top:100px;color:var(--white);font-family:"Open Sans",sans-serif;font-style:italic;font-weight:700;font-size:25px}
  .contact{position:absolute;left:390px;top:250px;width:500px;height:230px;border:4px solid var(--white);border-radius:32px;background:linear-gradient(180deg,var(--blue-mid),var(--blue-deep));color:var(--white);font-family:"Signika",sans-serif;text-align:center;padding-top:14px}
  .contact__lead{font-size:34px;font-weight:600}
  .contact__region{font-size:29px;font-weight:500;line-height:36px}
  .contact__phone{display:flex;align-items:center;justify-content:center;gap:16px;margin-top:8px;font-size:58px;font-weight:600}
  .contact__phone svg{width:70px;height:60px}
  .abn{position:absolute;left:34px;bottom:30px;font-family:"Open Sans",sans-serif;font-weight:800;font-size:24px;color:var(--ink)}
</style>
</head>
<body>
<main class="canvas">

  <section class="card card--back" aria-label="Card back – services">
    <div class="photo" role="img" aria-label="Photo of cleaned pebblecrete driveway" style="left:0;top:150px;width:480px;height:390px;background:linear-gradient(90deg,var(--pebble-a),var(--pebble-b))"></div>
    <div class="photo" role="img" aria-label="Photo of brick wall with vine removal" style="left:480px;top:150px;width:480px;height:390px;background:linear-gradient(135deg,var(--brick-a),var(--brick-b))"></div>
    <svg class="card-art" viewBox="0 0 960 540" aria-hidden="true">
      <defs>
        <linearGradient id="backBlue" x1="0" y1="0" x2="1" y2="1">
          <stop offset="0" stop-color="#2a4fb0"/>
          <stop offset=".55" stop-color="#23409e"/>
          <stop offset="1" stop-color="#1b2f86"/>
        </linearGradient>
      </defs>
      <path d="M0 0H960V250C760 205 560 320 330 265C200 235 90 200 0 215Z" fill="var(--blue-light)" opacity=".85"/>
      <path d="M0 0H960V230C760 195 560 290 330 245C200 220 90 185 0 195Z" fill="url(#backBlue)"/>
    </svg>
    <div class="services">
      <p class="services__title">Services that we offer</p>
      <p class="services__line">Driveway | Foot Path Cleaning Treatment | Removal Of Moss</p>
      <p class="services__line">Mould Entertainment | Deck Area's Pebble Crete | cemented Area's Factory</p>
      <p class="services__line">Office Fronts House Exterior (Windows, Veranda's, Brick Work) Roof</p>
      <p class="services__line">Gutter Cleaning Roof Restoration - Brightwell, Solvane Roof Shield 417</p>
      <p class="services__licence">(Brightwell Application Licence, Includes Full 10 Year Warranty)</p>
    </div>
  </section>

  <section class="card card--front" aria-label="Card front – contact">
    <svg class="card-art" viewBox="0 0 960 540" aria-hidden="true">
      <defs>
        <linearGradient id="frontBlue" x1="0" y1="0" x2="1" y2="1">
          <stop offset="0" stop-color="#2c5fc0"/>
          <stop offset=".6" stop-color="#2446a6"/>
          <stop offset="1" stop-color="#1b2f86"/>
        </linearGradient>
        <linearGradient id="roofPhoto" x1="0" y1="0" x2="1" y2="1">
          <stop offset="0" stop-color="var(--tree)"/>
          <stop offset=".3" stop-color="var(--roof-a)"/>
          <stop offset="1" stop-color="var(--roof-b)"/>
        </linearGradient>
      </defs>
      <rect width="960" height="540" fill="url(#frontBlue)"/>
      <path d="M0 170C250 150 500 190 960 330V540H0Z" fill="var(--white)"/>
      <path d="M0 192C230 178 380 220 520 300C640 370 700 460 760 540H0Z" fill="url(#roofPhoto)" role="img" aria-label="Photo of worker restoring a metal roof"/>
      <path d="M760 540C800 500 870 470 960 470V540Z" fill="var(--blue-mid)"/>
    </svg>
    <h1 class="brand">KESTREL SURFACE CLEANING</h1>
    <p class="tagline">Washing Water Blasting And Roof Restorations</p>
    <div class="contact">
      <p class="contact__lead">Contact Liam For A Free Quote</p>
      <p class="contact__region">Newcastle Region Hunter Valley Region</p>
      <p class="contact__region">Nelson Bay Region</p>
      <p class="contact__phone">
        <svg viewBox="0 0 70 60" aria-hidden="true">
          <path d="M4 20C4 8 66 8 66 20V26H50V20H20V26H4Z" fill="var(--white)"/>
          <path d="M18 26H52L62 54H8Z" fill="var(--white)"/>
          <circle cx="35" cy="40" r="9" fill="var(--blue-deep)"/>
          <circle cx="35" cy="40" r="4" fill="var(--white)"/>
        </svg>
        <span># 0412958364</span>
      </p>
    </div>
    <p class="abn">ABN# 48 217 903 561</p>
  </section>

</main>
</body>
</html>
```